Updates

Please take these words out of the flyer " or any other fees whatsoever." Added Monday, August 8, 2016

Industry/Entity Type

Real Estate

Font styles to use
Serif

Requirements
Must have

```html
<!DOCTYPE html>
<html lang="en">
<head>
<meta charset="utf-8">
<title>Summit Keystone Realty – 3 Commissioning Plans</title>
<link rel="stylesheet" href="https://fonts.googleapis.com/css2?family=Oswald:wght@500;600;700&family=Arimo:wght@400;700&family=Montserrat:wght@600&display=swap">
<style>
  :root{
    --stage:#141414;
    --red:#c8202a;
    --charcoal:#3a3a3c;
    --charcoal-dark:#2b2b2d;
    --maroon:#3a0a0c;
    --ink:#2e2e30;
    --white:#ffffff;
  }
  *{box-sizing:border-box;margin:0;padding:0}
  html,body{width:1200px;height:960px;overflow:hidden;background:var(--stage)}
  .flyer{position:absolute;left:246px;top:21px;width:710px;height:918px;background:var(--white);overflow:hidden;font-family:"Arimo",Arial,sans-serif}
  .hero-photo{position:absolute;left:0;top:0;width:710px;height:482px;
    background:
      radial-gradient(ellipse at 30% 30%, rgba(255,255,255,.95), rgba(255,255,255,0) 55%),
      linear-gradient(90deg,#f3f1ee 0%,#e9e3da 38%,#8c96a3 58%,#2f3e55 75%,#1b2638 100%);}
  .brand{position:absolute;left:0;width:364px;top:84px;text-align:center}
  .brand-mark{display:block;width:30px;height:30px;background:var(--ink);margin:0 auto 38px}
  .brand-name{font-family:"Montserrat",Arial,sans-serif;font-weight:600;font-size:24px;color:var(--red);line-height:1}
  .brand-tag{font-family:"Montserrat",Arial,sans-serif;font-weight:600;font-size:11px;color:var(--ink);margin-top:10px;letter-spacing:.5px}
  .headline{position:absolute;font-family:"Oswald",Arial,sans-serif;font-weight:700;line-height:1;letter-spacing:-1px;font-size:48px;transform:scaleX(.82);transform-origin:left}
  .headline-top{left:20px;top:384px;color:var(--red)}
  .headline-bottom{left:190px;top:436px;color:var(--ink)}
  .panels{position:absolute;left:0;top:478px}
  .plan-tag{position:absolute;height:34px;padding:0 18px;font-size:20px;line-height:34px;color:var(--white)}
  .plan-tag sup{font-size:11px}
  .plan-tag.dark{background:var(--charcoal-dark)}
  .plan-tag.red{background:var(--red)}
  .price{position:absolute;color:var(--white);white-space:nowrap;font-size:18px;line-height:30px;height:30px}
  .price b{font-family:"Oswald",Arial,sans-serif;font-weight:600;font-size:27px}
  .bullet{position:absolute;color:var(--white);white-space:nowrap;line-height:24px;font-size:16px}
  .bullet::before{content:"";position:absolute;left:-15px;top:9px;width:6px;height:6px;border-radius:50%;background:var(--white)}
  .bullet.wrap{font-size:14px;line-height:17px}
  .bullet.wrap::before{top:5px;width:5px;height:5px}
  .bullet.wrap.large{font-size:16px;line-height:20px}
  .bullet.wrap.large::before{top:7px;width:6px;height:6px}
  .contact{position:absolute;left:0;top:807px;width:366px;text-align:center;color:var(--white);font-family:"Oswald",Arial,sans-serif;font-weight:500;line-height:23px}
  .contact .label{font-size:16px}
  .contact .person{font-size:19px}
  .footer-band{position:absolute;left:0;top:885px;width:710px;height:33px;background:var(--charcoal-dark);color:var(--white);text-align:center;font-family:"Oswald",Arial,sans-serif;font-weight:500;font-size:18px;line-height:33px}
</style>
</head>
<body>
<main class="flyer">
  <div class="hero-photo" role="img" aria-label="Businessman in a suit holding a tablet, overlaid with a night city skyline and a rising growth chart"></div>

  <div class="brand">
    <span class="brand-mark"></span>
    <div class="brand-name">Summit Keystone Realty</div>
    <div class="brand-tag">Homes Built on Trust</div>
  </div>

  <h1>
    <span class="headline headline-top">3 COMMISSIONING</span>
    <span class="headline headline-bottom">PLANS</span>
  </h1>

  <svg class="panels" width="710" height="407" viewBox="0 0 710 407" aria-hidden="true">
    <rect x="0" y="0" width="710" height="407" fill="#ffffff"/>
    <polygon points="0,4 401,4 365,324 0,324" fill="var(--red)"/>
    <polygon points="0,324 365,324 355,407 0,407" fill="var(--maroon)"/>
    <polygon points="409,4 710,4 710,407 361,407" fill="var(--charcoal)"/>
  </svg>

  <div class="plan-tag dark" style="left:27px;top:482px">The 1<sup>st</sup> plan is</div>
  <div class="price" style="left:27px;top:539px"><b>100%</b> Commission</div>
  <div class="price" style="left:27px;top:572px"><b>99</b> Dollars a month</div>
  <div class="price" style="left:27px;top:604px"><b>$249</b> Per transaction</div>
  <div class="bullet" style="left:50px;top:647px;font-size:17px">No office fees,</div>
  <div class="bullet" style="left:50px;top:671px;font-size:17px">No franchise fees,</div>
  <div class="bullet wrap large" style="left:50px;top:713px">Computers available with Nordsoft office<br>professional internet access and Centrally</div>

  <div class="plan-tag red" style="left:423px;top:482px">The 2<sup>nd</sup> plan is</div>
  <div class="price" style="left:411px;top:540px"><b>90/10</b> for <b>$69</b> per month.</div>
  <div class="bullet" style="left:434px;top:575px">No office fees,</div>
  <div class="bullet" style="left:434px;top:599px">No franchise fees,</div>
  <div class="bullet wrap" style="left:431px;top:633px">Computers available with Nordsoft office<br>professional internet access and Centrally</div>

  <div class="plan-tag red" style="left:382px;top:702px">The 3<sup>rd</sup> plan is</div>
  <div class="bullet" style="left:417px;top:750px">No office fees,</div>
  <div class="bullet" style="left:417px;top:774px">No franchise fees,</div>
  <div class="bullet wrap" style="left:414px;top:807px">Computers available with Nordsoft office<br>professional internet access and Centrally</div>

  <div class="contact">
    <div class="label">Contact</div>
    <div class="person">Marina Holloway Broker</div>
    <div class="person">Owner 214-555-0147</div>
  </div>

  <div class="footer-band">Centrally located 4820 Meadow Crest Dr, Arlington, TX 76006 1st floor 212</div>
</main>
</body>
</html>
```